IT business looking for Standout Letterhead Design

We need a letterhead design for a company based in San Diego, CA called Corvane Systems, Inc. We specialize in IT engineering, installation and technical support pertaining to the department of defense.

We would like to see a design that incorporates the black and gold that matches our company logo.

More information on the company can be found at www.corvane-sys.example

```html
<!DOCTYPE html>
<html lang="en">
<head>
<meta charset="utf-8">
<title>Corvane Systems, Inc. – Letterhead</title>
<link rel="stylesheet" href="https://fonts.googleapis.com/css2?family=Libre+Baskerville:wght@400;700&family=Open+Sans:wght@700&family=Ubuntu:wght@700&display=swap">
<style>
  :root {
    --ink: #1e1b1a;
    --gold: #8f8418;
    --paper: #ffffff;
    --rule: #2a2a2a;
    --emblem: #ecebe7;
    --frame: #bdbdbd;
  }
  html, body { margin: 0; padding: 0; overflow: hidden; background: var(--paper); }
  .letterhead {
    position: relative;
    width: 843px;
    height: 1200px;
    overflow: hidden;
    background: var(--paper);
    box-sizing: border-box;
    border: 1px solid var(--frame);
    font-family: "Libre Baskerville", serif;
    color: var(--ink);
  }
  .masthead-shape { position: absolute; left: 0; top: 0; }
  .brand-mark {
    position: absolute;
    left: 10px; top: 30px;
    font-family: "Libre Baskerville", serif;
    font-weight: 400;
    font-size: 15px;
    letter-spacing: 0.5px;
    color: var(--ink);
  }
  .company-title {
    position: absolute;
    left: 164px; width: 520px; top: 4px;
    text-align: center;
    font-family: "Ubuntu", sans-serif;
    font-weight: 700;
    font-size: 24px;
    color: var(--gold);
  }
  .tagline-bar {
    position: absolute;
    left: 0; right: 0; top: 61px; height: 15px;
    background: var(--ink);
    text-align: center;
    font-family: "Open Sans", sans-serif;
    font-weight: 700;
    font-size: 11.5px;
    line-height: 15px;
    color: var(--gold);
  }
  .field {
    position: absolute;
    top: 108px;
    font-size: 14px;
    display: flex;
    align-items: flex-end;
  }
  .field .blank { display: inline-block; border-bottom: 1px solid var(--ink); width: 83px; margin-left: 6px; margin-bottom: 4px; }
  .field-date { left: 22px; }
  .field-ref { right: 5px; }
  .field-ref .blank { margin-left: 2px; }
  .emblem {
    position: absolute;
    left: 272px; top: 432px;
    width: 300px; height: 300px;
    border-radius: 50%;
    background: var(--emblem);
  }
  .footer-name {
    position: absolute;
    left: 0; right: 0; top: 1142px;
    text-align: center;
    font-weight: 700;
    font-size: 13.5px;
    color: var(--ink);
  }
  .footer-band {
    position: absolute;
    left: 0; right: 0; bottom: 0; height: 40px;
    background: var(--ink);
    text-align: center;
    font-weight: 700;
    font-size: 13.5px;
    line-height: 17px;
    padding-top: 3px;
    box-sizing: border-box;
    color: var(--gold);
  }
</style>
</head>
<body>
  <main class="letterhead">
    <svg class="masthead-shape" width="843" height="60" viewBox="0 0 843 60" aria-hidden="true">
      <polygon points="98,0 754,0 684,45 164,45" fill="var(--ink)"/>
    </svg>
    <div class="brand-mark">CORVANE</div>
    <div class="company-title">Corvane Systems Inc.</div>
    <div class="tagline-bar">Deals in IT Engineering, Installation &amp; Technical Support</div>

    <div class="field field-date">Date: <span class="blank"></span></div>
    <div class="field field-ref">Reference #:<span class="blank"></span></div>

    <div class="emblem" aria-hidden="true"></div>

    <div class="footer-name">Corvane Systems, Incorporation, San Diego, CA</div>
    <footer class="footer-band">
      Phone: 619-555-0142, Facsimile: 619-555-0187<br>
      www.corvane-sys.example, e-mail: info@corvane-sys.example
    </footer>
  </main>
</body>
</html>
```